Gum Creek Critters business card and social media card

I would like 2 designs,

one with my logo that I have (attached file) for the front and then the chatterbook, Snapgallery and wanderguide icons on the back.I would like it to be eye catching.

The second design i would like the designers to come up with.I am looking for a colorful and eye catching but easy to read business card. I am in the center of Australia and would like earthy colors like orange/red, yellow, charcoal, brown, green etc. I would like a blue tongue lizard and a king brown snake in the design for the front. For the back I would like the Chatterbook, Snapgallery and wander guide logos.

Industry/Entity Type

Business

Contact Information for Business Card

Marcus Toller
CEO
GUM CREEK CRITTERS pty ltd
W: 041 907 2286
M: 048 216 0947
E: marcus@gumcreekcritters-example.com.au

Font styles to use
Other font styles liked:
• chiller

Colors
f37122
fbed22
ec1f27
474747
0492cd
acd036

Requirements
Must have
• Business name or my logo (attached file)
• Gum Creek Critters (in a cool font, like "chiller")
• Chatterbook icon
• Snapgallery icon
• Wanderguide icon
Nice to have
• Snake and a blue tongue lizard (either the full animals or just the heads)

```html
<!DOCTYPE html>
<html lang="en">
<head>
<meta charset="utf-8">
<title>Gum Creek Critters – Business Card</title>
<link href="https://fonts.googleapis.com/css2?family=Roboto:wght@400;500&family=Roboto+Condensed:wght@700&display=swap" rel="stylesheet">
<style>
  :root{
    --stage:#ecebe8;
    --card-white:#ffffff;
    --card-red:#d4243f;
    --brand-red:#d9243f;
    --brand-orange:#f39a1c;
    --ink:#4a4a4a;
    --white:#ffffff;
  }
  *{box-sizing:border-box;margin:0;padding:0}
  html,body{width:1200px;height:886px;overflow:hidden}
  body{background:var(--stage);font-family:'Roboto',sans-serif;position:relative}
  .card{
    position:absolute;top:133px;width:380px;height:620px;border-radius:22px;
    box-shadow:0 10px 30px rgba(0,0,0,.18);
  }
  .card--front{left:170px;background:var(--card-white);text-align:center}
  .card--back{left:650px;background:var(--card-red)}

  .brand{
    position:absolute;left:50%;transform:translateX(-50%);
    display:flex;align-items:center;gap:10px;white-space:nowrap;
    font-family:'Roboto Condensed',sans-serif;font-weight:700;font-size:30px;letter-spacing:.5px;
  }
  .brand__dot{width:16px;height:16px;border-radius:50%;flex:none}
  .card--front .brand{top:95px;color:var(--brand-red)}
  .card--front .brand__dot{background:var(--brand-orange)}
  .card--back .brand{top:255px;color:var(--white)}
  .card--back .brand__dot{background:var(--white)}

  .creature-band{
    position:absolute;left:60px;right:60px;height:26px;border-radius:13px;
    background:linear-gradient(90deg,#f39a1c,#e8c21e);
  }
  .card--front .creature-band{top:150px}
  .card--back .creature-band{top:310px;opacity:.9}

  .person{position:absolute;top:222px;left:0;right:0}
  .person svg{width:18px;height:14px;fill:var(--brand-red)}
  .person__name{
    font-family:'Roboto Condensed',sans-serif;font-weight:700;font-size:32px;
    color:var(--brand-red);letter-spacing:.5px;line-height:1.1;margin-top:4px;
  }
  .person__role{font-size:15px;font-weight:500;color:var(--brand-orange)}

  .contacts{position:absolute;top:330px;left:0;right:0;list-style:none}
  .contacts li{font-size:16px;color:var(--ink);line-height:20px;margin-bottom:10px}
  .contacts svg{display:block;margin:0 auto 2px;width:14px;height:14px;fill:var(--brand-red)}
  .contacts .company{font-size:13px;letter-spacing:.5px}

  .social{position:absolute;left:30px;right:30px;bottom:100px;display:flex;align-items:center;gap:8px}
  .social__rule{flex:1;height:1px;background:rgba(255,255,255,.55)}
  .social__icon{width:30px;height:30px;border-radius:50%;border:2px solid var(--white)}
</style>
</head>
<body>

<section class="card card--front" aria-label="Business card front">
  <div class="brand"><span class="brand__dot"></span>Gum Creek Critters</div>
  <div class="creature-band" role="img" aria-label="Illustration of a blue tongue lizard and a king brown snake"></div>

  <div class="person">
    <svg viewBox="0 0 18 14"><circle cx="9" cy="4" r="4"/><rect x="1" y="9" width="16" height="5" rx="2"/></svg>
    <div class="person__name">MARCUS TOLLER</div>
    <div class="person__role">CEO</div>
  </div>

  <ul class="contacts">
    <li class="company">
      <svg viewBox="0 0 14 14"><path d="M7 0a5 5 0 0 1 5 5c0 4-5 9-5 9S2 9 2 5a5 5 0 0 1 5-5zm0 3a2 2 0 1 0 0 4 2 2 0 0 0 0-4z"/></svg>
      GUM CREEK CRITTERS pty ltd
    </li>
    <li>
      <svg viewBox="0 0 14 14"><path d="M3 0l3 3-2 2c1 2 3 4 5 5l2-2 3 3-2 3C6 14 0 8 0 3z"/></svg>
      041 907 2286
    </li>
    <li>
      <svg viewBox="0 0 14 14"><path d="M3 0h8v14H3zM4.5 1.5v9h5v-9z"/></svg>
      048 216 0947
    </li>
    <li>
      <svg viewBox="0 0 14 14"><path d="M0 2h14v10H0zM1 3l6 5 6-5z" fill-rule="evenodd"/></svg>
      marcus@gumcreekcritters-example.com.au
    </li>
    <li>
      <svg viewBox="0 0 14 14"><circle cx="7" cy="7" r="7"/></svg>
      gumcreekcritters-example.com.au
    </li>
  </ul>
</section>

<section class="card card--back" aria-label="Business card back">
  <div class="brand"><span class="brand__dot"></span>Gum Creek Critters</div>
  <div class="creature-band" role="img" aria-label="Illustration of a lizard and a snake wrapping the name"></div>

  <div class="social" aria-label="Chatterbook, Snapgallery and Wanderguide">
    <span class="social__rule"></span>
    <span class="social__icon" aria-label="Chatterbook"></span>
    <span class="social__icon" aria-label="Snapgallery"></span>
    <span class="social__icon" aria-label="Wanderguide"></span>
    <span class="social__rule"></span>
  </div>
</section>

</body>
</html>
```